Introduction flyer

Bright Orchard Nutrition & Wellness Consulting, is a new holistic nutritional therapy specialising in womens health. I want a flyer that appeals to women between 15 to 60. It must speak "health, food & balance". I have attached the basic info I need included in the text. I like Greens & Blues, soft text. My flyer will be distributed to cafes, shops, fitness centres, hung up in grocery stores & health centres etc. The QEVR & WRUK logos need to appear on the flyer to show I am fully registered. My own logo & company name is attached.

Target Market(s)

Women from 10 to 60 years old.

Industry/Entity Type

Nutritionist

Colors
32a6d7
abd037
33b8a4
fbf289
ffcf3e
b768aa
d5d5d5
dcdcdc
e8e8e8

Requirements
Must have
• An image of healthy food & ladies. A group of women eating soup, stews or curry type dishes, with plenty of colour - no bread or white wine, and not just fruit please. Food that looks enjoyable to the average person.
• Nutrition is main part of my job, so please keep that in mind & emphasise food & natural well being.
Should not have
• People exercising, men, white wine, bread, cakes, sweets etc..

```html
<!DOCTYPE html>
<html lang="en">
<head>
<meta charset="utf-8">
<title>Bright Orchard Nutrition &amp; Wellness Consulting – Flyer</title>
<link href="https://fonts.googleapis.com/css2?family=Tinos:wght@400;700&family=Lato:wght@400;700&family=Bebas+Neue&display=swap" rel="stylesheet">
<style>
:root{
  --green:#0f8a3a;
  --green-dark:#0b6e2c;
  --green-bright:#2fbf4a;
  --blue:#1a5fb4;
  --blue-deep:#0d3f8f;
  --blue-mid:#2566c2;
  --ink:#1b1b1b;
  --paper:#ffffff;
  --paper-soft:#f1f2f2;
  --backdrop:#9a9a9a;
}
*{margin:0;padding:0;box-sizing:border-box}
html,body{width:1200px;height:1200px;overflow:hidden;background:var(--backdrop)}
.flyer{position:absolute;left:183px;top:15px;width:833px;height:1170px;background:linear-gradient(#fff,var(--paper-soft));overflow:hidden;font-family:"Lato",sans-serif;color:var(--ink)}
.photo{position:absolute;left:0;top:0;width:833px;height:440px;
  background:linear-gradient(90deg,#ffffff 0%,rgba(255,255,255,.85) 18%,rgba(255,255,255,0) 45%),
  linear-gradient(180deg,#e9e3d6 0%,#b9c9a6 45%,#7fa46d 75%,#5c8a55 100%)}
.photo-people{position:absolute;left:300px;top:0;width:480px;height:440px;
  background:radial-gradient(ellipse at 45% 40%,rgba(240,210,190,.8) 0%,rgba(70,110,190,.55) 45%,rgba(70,110,190,0) 75%)}
.wave{position:absolute;left:0;top:300px;width:833px;height:155px}
.brand{position:absolute;left:4px;top:95px;width:340px;text-align:center}
.brand-dot{display:inline-block;width:50px;height:50px;border-radius:50%;background:var(--blue-mid);margin-bottom:6px}
.brand-name{font-family:"Tinos",serif;font-weight:400;color:var(--blue);font-size:17px;line-height:20px;letter-spacing:1px;white-space:nowrap}
.center{position:absolute;left:0;width:833px;text-align:center;font-family:"Tinos",serif;line-height:1.15}
.q-head{top:456px;font-weight:700;color:var(--green);font-size:30px}
.q-sub{top:495px;color:var(--blue-mid);font-size:19px}
.q-big{top:518px;color:var(--green);font-size:37px;letter-spacing:.5px;font-weight:400}
.diet{position:absolute;left:34px;top:570px;font-family:"Tinos",serif;font-weight:700;font-size:24px;line-height:31px}
.diet .l1{color:var(--blue-mid)}
.diet .l2{color:var(--green)}
.tagline{position:absolute;left:34px;top:634px;font-size:19px;color:var(--ink)}
.intro{position:absolute;left:34px;top:666px;width:477px;font-size:12.6px;line-height:16.3px;text-align:justify;color:#222}
.visits{position:absolute;left:549px;top:578px;width:242px;height:175px;border-radius:26px;border:5px solid var(--green-dark);background:#fff;padding:4px}
.visits-inner{width:100%;height:100%;border-radius:20px;background:radial-gradient(circle at 50% 40%,#2d74d6,var(--blue-deep));text-align:center;padding-top:26px}
.visits .big{font-family:"Bebas Neue",sans-serif;color:#fff;font-size:27px;line-height:30px;white-space:nowrap}
.visits .small{color:var(--green-bright);font-size:12.5px;line-height:17px;white-space:nowrap}
.visits .gap{margin-top:4px}
.qual{position:absolute;left:34px;top:768px;font-family:"Tinos",serif;font-weight:700;font-size:24.5px;line-height:31px}
.qual .l1{color:var(--green)}
.qual .l2{color:var(--blue-mid)}
.band{position:absolute;left:0;top:842px;width:833px;height:164px;background:linear-gradient(90deg,var(--green-dark),#129a40 50%,var(--green-dark));border-top:3px solid #fff;outline:2px solid var(--green-dark)}
.band ul{list-style:none;position:absolute;top:16px;color:#fff;font-size:13.5px;line-height:16.5px}
.band li{position:relative;padding-left:18px;margin-bottom:16px}
.band li::before{content:"";position:absolute;left:2px;top:4px;width:7px;height:7px;border-radius:50%;background:#d8f0dc}
.col1{left:34px;width:270px}
.col2{left:363px;width:220px}
.col3{left:613px;width:210px}
.contact{position:absolute;left:27px;top:1022px;width:243px;height:114px;border-radius:22px;border:5px solid var(--green-bright);background:#fff;padding:3px}
.contact-inner{width:100%;height:100%;border-radius:17px;background:radial-gradient(circle at 50% 40%,#2d74d6,var(--blue-deep));text-align:center;color:#fff;font-family:"Tinos",serif;font-weight:700;padding-top:9px}
.contact .lbl{font-size:12px}
.contact .phone{font-size:28px;line-height:32px}
.contact .or{font-size:12px;margin-top:4px}
.contact .mail{font-size:12px}
.book{position:absolute;left:292px;top:1033px;width:262px;text-align:center;font-family:"Tinos",serif;font-weight:700;font-size:18px;line-height:23px;color:var(--green-dark)}
.book .blue{color:var(--blue-mid)}
.notes{position:absolute;left:576px;top:1035px;width:221px;font-size:11.3px;line-height:14.7px;text-align:justify;text-align-last:center;color:#222}
.base{position:absolute;left:0;bottom:0;width:833px;height:14px;background:#2a2a2a}
</style>
</head>
<body>
<main class="flyer">
  <div class="photo" role="img" aria-label="Photo of two smiling women embracing outdoors in a garden">
    <div class="photo-people"></div>
  </div>
  <svg class="wave" viewBox="0 0 833 155" preserveAspectRatio="none" aria-hidden="true">
    <path d="M0 80 C70 50 160 25 200 55 C240 85 230 148 320 148 C420 148 500 40 560 15 C610 -5 600 145 650 145 C720 145 790 100 833 75 L833 155 L0 155 Z" fill="#ffffff"/>
    <path d="M0 80 C70 50 160 25 200 55 C240 85 230 148 320 148 C420 148 500 40 560 15 C610 -5 600 145 650 145 C720 145 790 100 833 75" fill="none" stroke="#0f8a3a" stroke-width="4"/>
    <path d="M0 72 C70 42 160 17 202 47 C242 77 236 138 322 138 C420 138 500 30 560 7 C610 -12 606 135 652 135 C720 135 790 90 833 66" fill="none" stroke="#1a5fb4" stroke-width="9"/>
  </svg>

  <div class="brand">
    <span class="brand-dot"></span>
    <div class="brand-name">BRIGHT ORCHARD NUTRITION<br>&amp; Wellness Consulting</div>
  </div>

  <h1 class="center q-head">Do You Experience</h1>
  <p class="center q-sub">Low Energy, Low Libido, Menstrual Cycle Complications or</p>
  <h2 class="center q-big">ARE YOU PLANNING A BABY?</h2>

  <h3 class="diet"><span class="l1">Small Changes To Your Diet</span><br><span class="l2">May Lead To Big Changes In Your Health:</span></h3>
  <p class="tagline">Eat well, live well.</p>
  <p class="intro">Discover exactly what YOU need to change and how to make these changes long lasting. There is no 1 rule-fits-all. My nutritional advice aims to dig up the root cause to my client’s health concerns. My lifestyle plans are completely personalised to an individual’s needs and circumstances. I consider the whole person not just symptoms or disease.</p>

  <aside class="visits">
    <div class="visits-inner">
      <div class="big">HOME VISITS AVAILABLE</div>
      <div class="small">at no extra cost within local area;</div>
      <div class="big gap">I CAN VISIT YOUR PLACE</div>
      <div class="small">of work or home.</div>
    </div>
  </aside>

  <h3 class="qual"><span class="l1">Qualified, Registered and fully insured Nutritional Therapist &amp;</span><br><span class="l2">Wellness Consultant, specialising in:</span></h3>

  <section class="band">
    <ul class="col1">
      <li>Fertility, IVF, pre-conception, pregnancy &amp; post-natal care</li>
      <li>Menstrual cycle challenges<br>(PCOS, Endometriosis, PMS,<br>heavy/irregular periods etc)</li>
      <li>Thyroid conditions</li>
    </ul>
    <ul class="col2">
      <li>Low libido</li>
      <li>Digestive health</li>
      <li>Chronic fatigue syndrome</li>
    </ul>
    <ul class="col3">
      <li>Perimenopause/menopause</li>
      <li>Weight management</li>
      <li>Type 2 diabetes, blood sugar dysregulation, high blood pressure, high cholesterol</li>
    </ul>
  </section>

  <div class="contact">
    <div class="contact-inner">
      <div class="lbl">Call Maeve today on</div>
      <div class="phone">085-4407-219</div>
      <div class="or">or Email</div>
      <div class="mail">maeve@brightorchardnutrition.ie</div>
    </div>
  </div>

  <p class="book"><span class="blue">TO BOOK A CONSULTATION</span><br>OR FOR A FREE NO<br>OBLIGATION 15-MINUTE<br>MINI CONSULTATION.</p>

  <p class="notes">Initial consultations typically last up to 2 hours, follow-ups 30 – 60 minutes. Further investigative tests may be recommended such as blood, urine, salvia sampling. These will always be agreed with the client in advance.</p>

  <div class="base"></div>
</main>
</body>
</html>
```